Brightvale Fluid Systems Corp Business Cards

Business cards to match the logo.

Company is a start up water technology company that has developed a patented system using centrifugal force to separate waste from municipal waste water to produce crystal clear clean water. Product sell starting at 2 million to governments both in the US and international.

Business cards should have a professional look with the target generally engineers.

Target Market(s)

Engineers, Government officials and investors

Industry/Entity Type

Water Treatment

Contact Information for Business Card

Business cards design will be used for 6 to 8 people with job titles. Can use the quote "If there is magic in the planet, it is contained in water." but not required to use quote. Should follow theme of Logo

Font styles to use
Other font styles liked:
• match logo font

Requirements
Nice to have
• Colors to match Logo. Business cards to match style of flow of Logo.
• Emphasis on clean look not a busy look. Clean flowing water.
Should not have
• Pictures of industrial equipment or wastewater

```html
<!DOCTYPE html>
<html lang="en">
<head>
<meta charset="utf-8">
<title>Brightvale Fluid Systems Corp — Business Cards</title>
<link href="https://fonts.googleapis.com/css2?family=Montserrat:wght@400;500;600;700&display=swap" rel="stylesheet">
<style>
  :root {
    --stage: #3a3a3a;
    --navy: #21507a;
    --sky: #3aa3dc;
    --ink: #1c1c1c;
    --paper: #ffffff;
  }
  * { box-sizing: border-box; margin: 0; padding: 0; }
  html, body { width: 1200px; height: 1200px; overflow: hidden; }
  body {
    background: var(--stage);
    font-family: "Montserrat", sans-serif;
    display: flex;
    flex-direction: column;
    align-items: center;
    justify-content: center;
    gap: 52px;
  }
  .card {
    position: relative;
    width: 900px;
    height: 514px;
    overflow: hidden;
  }
  /* Front */
  .card-front { background: var(--navy); color: var(--paper); }
  .card-front .brand {
    position: absolute;
    left: 0; right: 0; top: 190px;
    display: flex; align-items: center; justify-content: center; gap: 18px;
  }
  .brand-dot {
    width: 22px; height: 22px; border-radius: 50%;
    background: var(--sky);
  }
  .brand-name {
    font-weight: 600;
    font-size: 44px;
    letter-spacing: 4px;
    text-transform: uppercase;
    line-height: 1.15;
    text-align: center;
  }
  .card-front .brand-name { color: var(--paper); }
  .quote {
    position: absolute;
    left: 0; right: 0; bottom: 58px;
    text-align: center;
    font-size: 19px;
    font-weight: 500;
    letter-spacing: 0.5px;
    text-transform: uppercase;
  }
  /* Back */
  .card-back { background: var(--paper); color: var(--ink); }
  .card-back .brand {
    position: absolute;
    right: 48px; top: 78px;
    display: flex; align-items: center; gap: 14px;
  }
  .card-back .brand-name {
    color: var(--navy);
    font-size: 30px;
    letter-spacing: 3px;
    text-align: left;
  }
  .card-back .brand-dot { width: 16px; height: 16px; }
  .person { position: absolute; left: 88px; top: 120px; }
  .person-name { color: var(--sky); font-size: 31px; font-weight: 700; }
  .person-title { font-size: 21px; font-weight: 500; margin-top: 4px; }
  .address {
    position: absolute; left: 88px; top: 268px;
    font-size: 21px; font-weight: 500; line-height: 1.3;
  }
  .contacts {
    position: absolute; left: 88px; top: 344px;
    list-style: none; font-size: 21px; font-weight: 500;
  }
  .contacts li { display: flex; align-items: center; gap: 18px; height: 30px; }
  .contacts svg { width: 20px; height: 20px; fill: var(--sky); flex: none; }
  .footer-band {
    position: absolute; left: 0; bottom: 26px;
    width: 900px; height: 42px;
  }
  .website {
    position: absolute; left: 66px; bottom: 32px;
    color: var(--paper); font-size: 20px; font-weight: 500; letter-spacing: 0.5px;
  }
</style>
</head>
<body>

  <section class="card card-front" aria-label="Card front">
    <div class="brand">
      <span class="brand-dot"></span>
      <span class="brand-name">Brightvale Fluid<br>Systems</span>
    </div>
    <p class="quote">If there is magic in the planet, it is contained in water.</p>
  </section>

  <section class="card card-back" aria-label="Card back">
    <div class="person">
      <p class="person-name">Daniel Hartwell</p>
      <p class="person-title">Manager</p>
    </div>

    <div class="brand">
      <span class="brand-dot"></span>
      <span class="brand-name">Brightvale Fluid<br>Systems</span>
    </div>

    <p class="address">418 Cedar Bend Road<br>Austin, TX 78745</p>

    <ul class="contacts">
      <li>
        <svg viewBox="0 0 24 24" aria-hidden="true"><path d="M6.6 10.8a15.1 15.1 0 0 0 6.6 6.6l2.2-2.2a1 1 0 0 1 1-.25 11.4 11.4 0 0 0 3.6.57 1 1 0 0 1 1 1V20a1 1 0 0 1-1 1A17 17 0 0 1 3 4a1 1 0 0 1 1-1h3.5a1 1 0 0 1 1 1c0 1.25.2 2.45.57 3.57a1 1 0 0 1-.25 1z"/></svg>
        512 555 0142
      </li>
      <li>
        <svg viewBox="0 0 24 24" aria-hidden="true"><path d="M6 2h12v6H6zM4 9h16a2 2 0 0 1 2 2v6h-4v5H6v-5H2v-6a2 2 0 0 1 2-2zm4 7v4h8v-4z"/></svg>
        512 555 0143
      </li>
      <li>
        <svg viewBox="0 0 24 24" aria-hidden="true"><path d="M2 5h20v14H2zm2 2v.5l8 5.5 8-5.5V7l-8 5.5z"/></svg>
        info@brightvalefluid.com
      </li>
    </ul>

    <svg class="footer-band" viewBox="0 0 900 42" aria-hidden="true">
      <polygon points="0,0 796,0 786,42 0,42" fill="var(--navy)"/>
      <polygon points="812,0 852,0 842,42 802,42" fill="var(--sky)"/>
      <polygon points="868,0 900,0 900,42 858,42" fill="var(--navy)"/>
    </svg>
    <p class="website">www.brightvalefluid.com</p>
  </section>

</body>
</html>
```